依頼詳細
内覧会の予定日と移転開院日のお知らせチラシを作成していただきたいです。
記載項目
表面
・病院ロゴ
・病院名:くるみ台動物病院
・内覧会開催日時:4月1日、2日 10:00~16:00
・移転開院日:4月4日(月)
・住所:愛知県知立市栄花台5-27
・病院地図
・電話番号:0566-47-3958
・病院HP URL:https://kurumidai-ah.jp
・診療時間 月〜金曜 8:30~11:30 14:00~17:00
土曜日 8:30~11:30 14:00~18:00
日曜・祝日 休診
サイズ
A4
ページ数
片面
希望イメージ
シンプル 複雑
単色 カラフル
暗い 明るい
日常 高級
遊び心 厳粛
未来的 伝統的
女性的 男性的
希望する色
赤系、茶系、緑系、黄・オレンジ系
納品ファイル
• 高解像度JPG (.jpg)
• イラストレーター形式 (.ai)
• PNG形式 (.png)
補足説明
印刷はセルモアを利用する予定です。
移転先の場所を記載した画像を追加しました。

当院の移転時期が4月ということで春らしい桜を入れていただいた点と箱の上に犬と猫が乗っているというデザインの可愛らしさからこちらのご提案に決めさせていただきました。

みなさま、素敵なご提案をいただき、誠にありがとうございました。
どれも魅力的なご提案で最後まで選出に悩みました。今後もコンペをお願いする機会があるかと思いますが、何卒よろしくお願いいたします。

```html
<!DOCTYPE html>
<html lang="ja">
<head>
<meta charset="utf-8">
<title>くるみ台動物病院 移転のお知らせ</title>
<link href="https://fonts.googleapis.com/css2?family=M+PLUS+Rounded+1c:wght@500;700;800&display=swap" rel="stylesheet">
<style>
:root{
  --sky:#cfe8f4;
  --green:#3f9a3a;
  --green-dark:#2f7d2c;
  --wood:#d9b98a;
  --wood-dark:#a9814f;
  --board:#f6ecd2;
  --orange:#e8822a;
  --red:#d63a2a;
  --brown:#5a3b22;
  --yellow:#ffe45c;
  --grass:#6cb548;
  --tree-light:#8cc25a;
  --tree:#4e9c3c;
  --white:#ffffff;
  --ink:#333333;
  --line:#b9c7a8;
}
*{margin:0;padding:0;box-sizing:border-box}
html,body{width:848px;height:1200px;overflow:hidden}
body{font-family:"M PLUS Rounded 1c",sans-serif;background:var(--sky);color:var(--ink)}
.flyer{position:relative;width:848px;height:1200px;overflow:hidden;background:var(--sky)}
.abs{position:absolute}

.brand{left:36px;top:26px;display:flex;align-items:center;gap:20px}
.brand-mark{width:76px;height:76px;border-radius:50%;background:var(--green);flex:none}
.brand-name{font-size:58px;font-weight:800;color:var(--green);letter-spacing:2px;line-height:1;white-space:nowrap}
.brand-en{left:150px;top:106px;font-size:26px;font-weight:700;color:var(--green);letter-spacing:1px}
.cat-art{left:770px;top:56px;width:50px;height:88px;border-radius:6px;background:linear-gradient(180deg,#6b7884,#4d5a66)}

.board{left:34px;top:158px;width:780px;height:716px;background:var(--wood);border-radius:18px;border:6px solid var(--wood-dark)}
.post{left:390px;top:868px;width:68px;height:120px;background:var(--wood-dark)}
.panel{left:108px;top:200px;width:632px;height:636px;background:var(--board);border-radius:14px}

.notice-tag{left:254px;top:228px;width:340px;height:60px;border-radius:30px;background:var(--orange);color:var(--white);font-size:34px;font-weight:800;text-align:center;line-height:60px;letter-spacing:3px}
.preview-title{left:0;width:848px;top:306px;text-align:center;font-size:36px;font-weight:800;color:var(--brown);letter-spacing:3px;line-height:1.2}

.dates{left:150px;top:382px;width:560px;height:72px}
.year{position:absolute;left:4px;top:0;font-size:18px;font-weight:700;color:var(--brown)}
.day{position:absolute;top:24px;font-size:44px;font-weight:800;color:var(--red);line-height:1;white-space:nowrap}
.day small{font-size:16px;display:inline-block;width:24px;height:24px;border-radius:50%;background:var(--red);color:var(--white);text-align:center;line-height:24px;vertical-align:middle;margin-left:2px}
.day-1{left:0}.day-2{left:124px}
.time-labels{position:absolute;left:290px;top:4px;width:262px;font-size:14px;font-weight:700;color:var(--brown);display:flex;justify-content:space-between}
.time{position:absolute;left:286px;top:24px;font-size:42px;font-weight:800;color:var(--brown);line-height:1;white-space:nowrap}

.map{left:170px;top:470px;width:508px;height:270px;border-radius:10px;background:linear-gradient(135deg,#eef0f2,#d9dde2)}

.open-day{left:224px;top:766px;width:400px;height:54px;border-radius:27px;background:var(--green);color:var(--white);font-size:24px;font-weight:800;text-align:center;line-height:54px;white-space:nowrap}
.open-day em{font-style:normal;color:var(--yellow);font-size:32px}

.grass{left:0;top:958px;width:848px;height:92px;background:linear-gradient(180deg,var(--grass),var(--green-dark))}
.trees-left{left:52px;top:868px;width:240px;height:160px;border-radius:12px;background:linear-gradient(180deg,var(--tree-light),var(--tree))}
.trees-right{left:560px;top:888px;width:170px;height:140px;border-radius:12px;background:linear-gradient(180deg,var(--tree-light),var(--tree))}

.info{left:0;top:1050px;width:848px;height:150px;background:var(--white)}
.address{left:26px;top:1064px;font-size:22px;font-weight:700;color:var(--ink)}
.phone{left:26px;top:1096px;display:flex;align-items:center;gap:8px;font-size:30px;font-weight:800;color:var(--ink)}
.url{left:26px;top:1140px;display:flex;align-items:center;gap:8px;font-size:20px;font-weight:700;color:var(--ink)}
.note{left:26px;top:1176px;font-size:12px;color:#555}

.hours{left:432px;top:1064px;width:390px;border-collapse:collapse;font-size:15px;font-weight:700}
.hours th,.hours td{border:1px solid var(--line);height:30px;text-align:center}
.hours thead th{background:var(--green);color:var(--white)}
.hours tbody th{background:#e8f3dc;color:var(--green-dark);width:70px}
</style>
</head>
<body>
<div class="flyer">
  <div class="brand abs">
    <span class="brand-mark"></span>
    <span class="brand-name">くるみ台動物病院</span>
  </div>
  <div class="brand-en abs">Kurumidai Animal Hospital</div>

  <div class="post abs"></div>
  <div class="board abs" role="img" aria-label="木の看板"></div>
  <div class="cat-art abs" role="img" aria-label="看板の上に座る猫のイラスト"></div>
  <div class="panel abs"></div>

  <div class="notice-tag abs">移転のお知らせ</div>
  <div class="preview-title abs">内覧会開催日時</div>

  <div class="dates abs">
    <span class="year">2022年</span>
    <span class="day day-1">4/1<small>金</small></span>
    <span class="day day-2">4/2<small>土</small></span>
    <span class="time-labels"><span>OPEN</span><span>CLOSE</span></span>
    <span class="time">10:00〜16:00</span>
  </div>

  <div class="map abs" role="img" aria-label="移転先の病院周辺地図"></div>

  <div class="open-day abs">移転開院日は <em>4/4</em>(月) です!</div>

  <div class="grass abs" role="img" aria-label="芝生と寝そべる犬のイラスト"></div>
  <div class="trees-left abs" role="img" aria-label="木とリスのイラスト"></div>
  <div class="trees-right abs" role="img" aria-label="小さな木のイラスト"></div>

  <div class="info abs"></div>
  <div class="address abs">愛知県知立市栄花台5-27</div>
  <div class="phone abs">
    <svg width="26" height="26" viewBox="0 0 24 24" aria-hidden="true"><rect width="24" height="24" rx="5" fill="#3f9a3a"/><path d="M8 5l2 3-1.5 1.5c.8 1.8 2.2 3.2 4 4L14 12l3 2-1 3c-5 0-10-5-10-10z" fill="#fff"/></svg>
    <span>0566-47-3958</span>
  </div>
  <div class="url abs">
    <svg width="22" height="22" viewBox="0 0 24 24" aria-hidden="true"><circle cx="12" cy="12" r="10" fill="none" stroke="#3f9a3a" stroke-width="2"/><path d="M2 12h20M12 2c3 3 3 17 0 20M12 2c-3 3-3 17 0 20" fill="none" stroke="#3f9a3a" stroke-width="1.6"/></svg>
    <span>https://kurumidai-ah.jp</span>
  </div>
  <div class="note abs">日曜・祝日は休診です。診療対象動物：犬・猫（その他はご相談ください）</div>

  <table class="hours abs">
    <thead><tr><th></th><th>月〜金曜日</th><th>土曜日</th></tr></thead>
    <tbody>
      <tr><th>午前</th><td>8:30〜11:30</td><td>8:30〜11:30</td></tr>
      <tr><th>午後</th><td>14:00〜17:00</td><td>14:00〜18:00</td></tr>
    </tbody>
  </table>
</div>
</body>
</html>
```